Guiding the Evergreen Young Competitor:
A Family Roadmap for Nurturing Bold, Steady, and Resilient Daughters on Fields and Beyond.
📘 Book Cover Design Brief – “Guiding the Evergreen Young Competitor”

Project Title:
Design a bold, inspiring book cover for a best-selling book titled:
Guiding the Evergreen Young Competitor
Subtitle: A Family Roadmap for Nurturing Bold, Steady, and Resilient Daughters on Fields and Beyond

🎯 Audience:

Parents of female athletes ages 14–20 who want their daughters to build confidence, strength, resilience, and long-term success both in sports and in life.

This book should feel encouraging, empowering, and credible — NOT cheesy, childish, or overly academic.

📕 Design Tone & Style:

Powerful and professional — should feel like a best-selling book from a leading performance or parenting expert

Emotionally compelling — conveys hope, resilience, strength, and possibility

Visually modern and clean — avoid anything overly busy, cliché, or childish

Heroic/aspirational tone — think transformation, leadership, strong positioning

💡 Visual Direction / Ideas (Use as Inspiration, Not Limitation):

Strong, confident teenage female athlete imagery — adaptable beyond one specific sport

Symbolic visuals — e.g. athlete standing strong, on a starting line, looking bold into the future, silhouette, or power stance

Bold typography that feels clean and modern (e.g., Proxima Nova, Montserrat, Gotham, Bebas Neue, etc.)

A title that stands out clearly when viewed as a thumbnail on Bookvale

Color tones: Empowering, modern, and strong: think deep blues, greens, purples, or golds — avoid playful pastels or overly girly themes

Potential imagery: textured backgrounds, motion, bravery, development, strength, growth, sport/action overlays

🔥 What the Cover MUST Communicate:

✅ This is for parents who want strong, confident female athletes
✅ It’s a guidebook for personal development AND sports performance
✅ It’s about creating “UNSHAKEABLE” confidence — physically, mentally and emotionally
✅ The message is: You can help your daughter become her strongest, most confident self

📚 Back-of-Book Summary (for context):

"Guiding the Evergreen Young Competitor" is a parent's blueprint to building girls who are strong in body, confident in mind, and ready to lead on and off the field. Through simple strategies around strength training, mindset, nutrition, and character development, this book gives parents the tools to help their daughters stay injury-resistant, break through mental barriers, and unlock their full potential — in sports and in life.

✅ Deliverables:

Full cover design (front, back, spine) for paperback
High-resolution files (print-ready)
Source files (PSD, AI, etc.)
3D mockup versions of the book (standing, flat, stack)

Target Market(s)

Industry/Entity Type

Fitness

Font styles to use
Sans Serif

Colors
FFF300
FFF600
FEFA6F
FFFEC7
FFFEE8

Requirements
Must have
• Bold Font
Should not have
• I don't want an image of a female athlete. I want this to be font based.

```html
<!DOCTYPE html>
<html lang="en">
<head>
<meta charset="UTF-8">
<title>Guiding the Evergreen Young Competitor — Cover</title>
<link href="https://fonts.googleapis.com/css2?family=Montserrat:wght@500;600;700&family=Oswald:wght@600;700&display=swap" rel="stylesheet">
<style>
  :root {
    --page-bg: #ececec;
    --cover-black: #0b0b0b;
    --cover-charcoal: #1c1c1c;
    --gold-deep: #a8904c;
    --gold-mid: #c9b26a;
    --gold-light: #ede3a8;
    --white: #ffffff;
  }
  * { margin: 0; padding: 0; box-sizing: border-box; }
  html, body {
    width: 1200px;
    height: 1200px;
    overflow: hidden;
    background: var(--page-bg);
  }
  .book-cover {
    position: absolute;
    left: 248px;
    top: 71px;
    width: 705px;
    height: 1057px;
    background:
      radial-gradient(ellipse at 70% 20%, var(--cover-charcoal) 0%, transparent 60%),
      radial-gradient(ellipse at 20% 75%, #161616 0%, transparent 55%),
      var(--cover-black);
    overflow: hidden;
  }
  .gold-text {
    background: linear-gradient(90deg, var(--gold-deep) 0%, var(--gold-mid) 30%, var(--gold-light) 55%, var(--gold-mid) 80%, var(--gold-deep) 100%);
    -webkit-background-clip: text;
    background-clip: text;
    color: transparent;
  }
  .series-mark {
    position: absolute;
    top: 42px;
    left: 0;
    width: 100%;
    display: flex;
    flex-direction: column;
    align-items: center;
    gap: 12px;
  }
  .series-mark__dot {
    width: 56px;
    height: 56px;
    border-radius: 50%;
    border: 2px solid var(--gold-mid);
  }
  .series-mark__name {
    font-family: "Montserrat", sans-serif;
    font-weight: 700;
    font-size: 14px;
    letter-spacing: 1.5px;
    color: var(--white);
  }
  .hero-figure {
    position: absolute;
    left: 219px;
    top: 169px;
    width: 346px;
    height: 247px;
    background: radial-gradient(ellipse at 50% 50%, rgba(201,178,106,0.55) 0%, rgba(201,178,106,0.18) 50%, transparent 72%);
  }
  .title {
    position: absolute;
    inset: 0;
    text-transform: uppercase;
    font-weight: 700;
  }
  .title__lead {
    position: absolute;
    left: 55px;
    top: 372px;
    font-family: "Montserrat", sans-serif;
    font-size: 64px;
    line-height: 1;
    color: var(--white);
    letter-spacing: -0.5px;
    white-space: nowrap;
  }
  .title__key {
    position: absolute;
    left: 54px;
    top: 434px;
    width: 600px;
    height: 132px;
    display: block;
    overflow: visible;
  }
  .title__key-text {
    font-family: "Oswald", sans-serif;
    font-weight: 700;
    font-size: 156px;
  }
  .title__tail {
    position: absolute;
    left: 55px;
    top: 564px;
    font-family: "Montserrat", sans-serif;
    font-size: 55px;
    line-height: 1;
    color: var(--white);
    letter-spacing: -0.5px;
    white-space: nowrap;
  }
  .subtitle {
    position: absolute;
    left: 0;
    top: 680px;
    width: 100%;
    text-align: center;
    font-family: "Montserrat", sans-serif;
    font-weight: 500;
    font-size: 24px;
    line-height: 43px;
    letter-spacing: 3px;
    text-transform: uppercase;
    color: var(--gold-mid);
  }
  .subtitle__accent { color: var(--white); }
  .author {
    position: absolute;
    left: 0;
    top: 954px;
    width: 100%;
    text-align: center;
    font-family: "Oswald", sans-serif;
    font-weight: 600;
    font-size: 50px;
    letter-spacing: 3px;
    text-transform: uppercase;
    line-height: 1;
  }
</style>
</head>
<body>
  <main class="book-cover">
    <header class="series-mark">
      <span class="series-mark__dot"></span>
      <span class="series-mark__name">EVERGREEN COMPETITOR</span>
    </header>

    <div class="hero-figure" role="img" aria-label="Gold silhouette of a young athlete sprinting forward"></div>

    <h1 class="title" aria-label="Guiding the Evergreen Young Competitor">
      <span class="title__lead">Guiding the</span>
      <svg class="title__key" viewBox="0 0 600 132" aria-hidden="true">
        <defs>
          <linearGradient id="gold-sheen" x1="0" y1="0" x2="1" y2="0">
            <stop offset="0" stop-color="#a8904c"/>
            <stop offset="0.3" stop-color="#c9b26a"/>
            <stop offset="0.55" stop-color="#ede3a8"/>
            <stop offset="0.8" stop-color="#c9b26a"/>
            <stop offset="1" stop-color="#a8904c"/>
          </linearGradient>
        </defs>
        <text class="title__key-text" x="0" y="128" textLength="600" lengthAdjust="spacingAndGlyphs" fill="url(#gold-sheen)">EVERGREEN</text>
      </svg>
      <span class="title__tail">Young Competitor</span>
    </h1>

    <p class="subtitle">
      A Family Roadmap for<br>
      Nurturing <span class="subtitle__accent">Bold, Steady,</span><br>
      <span class="subtitle__accent">and Resilient</span> Daughters<br>
      on Fields and Beyond
    </p>

    <p class="author gold-text">Marlo Keene</p>
  </main>
</body>
</html>
```